I need a book cover for a 6x9 book. The front cover information (title and author) is below, and the back cover information will be given to the winning designer. I am wanting something vibrant and bright, and I am open to your creativity, but I do not want any pictures of people on the cover. Save room for the barcode on the back cover.
Title:
Oops! Wrong Turn?
Quiet Rooms Explained: Notes on Patient Gardening Habits
Author:
Marisol Tembe

```html
<!DOCTYPE html>
<html lang="en">
<head>
<meta charset="utf-8">
<title>Oops! Wrong Turn? — Book Cover</title>
<link href="https://fonts.googleapis.com/css2?family=Anton&family=Montserrat:wght@600;700;800&family=Nunito:wght@900&display=swap" rel="stylesheet">
<style>
  :root {
    --stage: #e6eaee;
    --blue-deep: #0c6fd0;
    --blue-mid: #2a9fe8;
    --blue-light: #8fd3f6;
    --sea: #4aaee0;
    --shore: #b8d9a8;
    --lime: #a8f01e;
    --ink: #0a0d10;
    --paper: #ffffff;
    --band: rgba(10, 14, 20, 0.82);
  }
  * { margin: 0; padding: 0; box-sizing: border-box; }
  html, body {
    width: 1200px; height: 871px; overflow: hidden;
    background: var(--stage);
  }
  .canvas {
    position: relative; width: 1200px; height: 871px;
    display: flex; align-items: center; justify-content: center;
  }
  .cover {
    position: relative; width: 547px; height: 820px; overflow: hidden;
    background: linear-gradient(180deg, var(--blue-deep) 0%, var(--blue-mid) 38%, var(--blue-light) 55%, var(--blue-mid) 100%);
  }
  .title-bubble {
    position: absolute; left: 118px; top: 70px; width: 348px; height: 112px;
  }
  .title-bubble svg { position: absolute; inset: 0; }
  .title-bubble__word {
    position: absolute; inset: 0; display: flex; align-items: center; justify-content: center;
    font-family: "Nunito", sans-serif; font-weight: 900; font-size: 84px;
    color: var(--ink); letter-spacing: -1px; padding-left: 12px;
  }
  .title-main {
    position: absolute; left: 0; right: 18px; top: 180px;
    text-align: right; font-family: "Anton", sans-serif; font-size: 86px;
    line-height: 1; color: var(--lime); letter-spacing: 1px;
    text-shadow: 0 3px 0 rgba(0, 40, 110, 0.45);
    z-index: 2;
  }
  .subtitle-band {
    position: absolute; left: 0; top: 250px; width: 330px; height: 92px;
    background: linear-gradient(90deg, var(--band) 0%, var(--band) 70%, rgba(10,14,20,0.25) 100%);
    padding: 16px 0 0 26px;
    font-family: "Montserrat", sans-serif; font-weight: 600; font-size: 17px;
    line-height: 1.4; color: var(--paper); font-style: italic;
  }
  .subtitle-band__accent { color: var(--lime); font-weight: 800; font-style: normal; }
  .scene-photo {
    position: absolute; left: 0; right: 0; top: 380px; height: 300px;
    background: linear-gradient(180deg, var(--blue-light) 0%, #d6eef8 40%, var(--shore) 52%, var(--sea) 62%, var(--blue-mid) 100%);
  }
  .author-band {
    position: absolute; left: 0; right: 0; bottom: 0; height: 140px;
    background: var(--ink);
    display: flex; align-items: center; justify-content: center;
    font-family: "Montserrat", sans-serif; font-weight: 700; font-size: 30px;
    letter-spacing: 7px; color: var(--lime); text-transform: uppercase;
  }
</style>
</head>
<body>
<main class="canvas">
  <section class="cover">
    <div class="scene-photo" role="img" aria-label="Soft-focus seaside photo with a hand writing a short handwritten phrase circled in red marker"></div>

    <div class="title-bubble">
      <svg viewBox="0 0 348 112" width="348" height="112" aria-hidden="true">
        <path d="M38 0 H326 Q348 0 348 22 V90 Q348 112 326 112 H38 Q16 112 16 90 V70 L0 78 L16 52 V22 Q16 0 38 0 Z" fill="#ffffff"/>
      </svg>
      <span class="title-bubble__word">Oops!</span>
    </div>

    <h1 class="title-main">WRONG TURN?</h1>

    <p class="subtitle-band">Quiet Rooms Explained:<br>Notes on <span class="subtitle-band__accent">Patient Gardening Habits</span></p>

    <p class="author-band">Marisol Tembe</p>
  </section>
</main>
</body>
</html>
```